Bi-Lingual Trash and Recycle Sign

Hello,

Pretty straight forward. I have not been able to find the exact sign we need for a property with trash and recycle guidelines. I've found close, but not complete. We are looking to have metal 12x18 street sign type signs made to provide these instructions. Attached is a sample taken from the web. I want to be sure to avoid conflicting with them so looking for the same wording but in our own. I'd also like to include our company logo, also attached in vector in horizontal and vertical for inclusion.

```html
<!DOCTYPE html>
<html lang="en">
<head>
<meta charset="utf-8">
<title>Recycle – Reciclar Sign</title>
<link rel="stylesheet" href="https://fonts.googleapis.com/css2?family=Montserrat:wght@800&family=Roboto+Slab:wght@700;800&display=swap">
<style>
  :root {
    --frame-green: #00953f;
    --bin-green: #279b43;
    --paper: #ffffff;
    --stop-red: #c8232c;
    --maroon: #4a1a2b;
    --plum: #6a2a42;
    --ink: #111111;
    --bag-blue: #a9cfe6;
  }
  html, body {
    margin: 0;
    padding: 0;
    width: 870px;
    height: 1200px;
    overflow: hidden;
    background: var(--paper);
  }
  .sign {
    position: relative;
    width: 870px;
    height: 1200px;
    box-sizing: border-box;
    border: 45px solid var(--frame-green);
    background: var(--paper);
  }
  .sign > * { position: absolute; }

  .brand {
    top: 88px;
    left: 0;
    width: 100%;
    display: flex;
    justify-content: center;
    align-items: center;
    gap: 16px;
  }
  .brand-mark {
    width: 34px;
    height: 34px;
    background: var(--plum);
  }
  .brand-name {
    font-family: "Roboto Slab", serif;
    font-weight: 700;
    font-size: 34px;
    letter-spacing: 1px;
    color: var(--ink);
  }

  .headline {
    top: 238px;
    left: 0;
    width: 100%;
    margin: 0;
    text-align: center;
    font-family: "Roboto Slab", serif;
    font-weight: 800;
    font-size: 57px;
    color: var(--frame-green);
    letter-spacing: 0.5px;
  }

  .bin-icon {
    top: 366px;
    left: 282px;
    width: 214px;
    height: 244px;
  }

  .rule-row {
    left: 83px;
    display: flex;
    align-items: center;
  }
  .rule-row.english { top: 685px; }
  .rule-row.spanish { top: 849px; }
  .no-word {
    font-family: "Montserrat", sans-serif;
    font-weight: 800;
    font-size: 104px;
    line-height: 76px;
    color: var(--stop-red);
    letter-spacing: -4px;
  }
  .no-bag {
    width: 78px;
    height: 78px;
    margin-left: 8px;
  }
  .rule-text {
    margin-left: 20px;
    font-family: "Montserrat", sans-serif;
    font-weight: 800;
    font-size: 36px;
    line-height: 46px;
    color: var(--maroon);
  }

  .divider {
    top: 806px;
    left: 83px;
    width: 612px;
    height: 1px;
    background: var(--stop-red);
  }

  .program {
    top: 1003px;
    left: 0;
    width: 100%;
    margin: 0;
    text-align: center;
    font-family: "Roboto Slab", serif;
    font-weight: 700;
    font-size: 43px;
    color: var(--plum);
    letter-spacing: 1.5px;
  }
</style>
</head>
<body>
<main class="sign">
  <div class="brand">
    <span class="brand-mark"></span>
    <span class="brand-name">HALBROOK MANAGEMENT</span>
  </div>

  <h1 class="headline">RECYCLE - RECICLAR</h1>

  <svg class="bin-icon" viewBox="0 0 214 244" aria-label="Recycling bin">
    <rect x="78" y="0" width="58" height="36" rx="14" fill="var(--bin-green)"/>
    <rect x="0" y="34" width="214" height="22" rx="6" fill="var(--bin-green)"/>
    <path d="M12 64 H202 L180 228 Q178 244 162 244 H52 Q36 244 34 228 Z" fill="var(--bin-green)"/>
    <g transform="translate(107 142)" fill="#ffffff">
      <g id="arrow">
        <path d="M-14 -44 L14 -44 L30 -16 L40 -22 L34 6 L8 -4 L18 -10 L6 -30 L-6 -30 L-16 -14 L-28 -22 Z"/>
      </g>
      <use href="#arrow" transform="rotate(120)"/>
      <use href="#arrow" transform="rotate(240)"/>
    </g>
  </svg>

  <div class="rule-row english">
    <span class="no-word">N</span>
    <svg class="no-bag" viewBox="0 0 78 78">
      <rect x="22" y="16" width="34" height="46" rx="10" fill="var(--bag-blue)" role="img" aria-label="Plastic bag"/>
      <circle cx="39" cy="39" r="33" fill="none" stroke="var(--stop-red)" stroke-width="10"/>
      <line x1="16" y1="16" x2="62" y2="62" stroke="var(--stop-red)" stroke-width="10"/>
    </svg>
    <div class="rule-text">PLASTIC<br>BAGS ACCEPTED</div>
  </div>

  <div class="divider"></div>

  <div class="rule-row spanish">
    <span class="no-word">N</span>
    <svg class="no-bag" viewBox="0 0 78 78">
      <rect x="22" y="16" width="34" height="46" rx="10" fill="var(--bag-blue)" role="img" aria-label="Bolsa plástica"/>
      <circle cx="39" cy="39" r="33" fill="none" stroke="var(--stop-red)" stroke-width="10"/>
      <line x1="16" y1="16" x2="62" y2="62" stroke="var(--stop-red)" stroke-width="10"/>
    </svg>
    <div class="rule-text">SE ACEPTAN<br>BOLSAS PLÁSTICAS</div>
  </div>

  <p class="program">SINGLE SORT RECYCLING</p>
</main>
</body>
</html>
```